Velmora Biz Card 2019

New business card for Velmora Property Inspections. We are a residential home inspection company in Arizona.

Target Market(s)

Real Estate

Font styles to use
Sans Serif

Requirements
Must have
• Glen Mirewick
• Home Inspector
• Velmora Property Inspections, LLC
• 480-555-0172
• glen@velmora-llc.example

```html
<!DOCTYPE html>
<html lang="en">
<head>
<meta charset="utf-8">
<title>Velmora Biz Card 2019</title>
<link rel="stylesheet" href="https://fonts.googleapis.com/css2?family=Lato:wght@400;700&family=Russo+One&display=swap">
<style>
  :root {
    --page: #ffffff;
    --card: #1c1c1c;
    --green: #3fb94a;
    --grey: #8a8a8a;
    --silver: #d9d9d9;
    --white: #ffffff;
  }
  * { margin: 0; padding: 0; box-sizing: border-box; }
  html, body { width: 1200px; height: 1200px; overflow: hidden; background: var(--page); }
  .canvas { position: relative; width: 1200px; height: 1200px; }
  .card {
    position: absolute; top: 180px; width: 480px; height: 840px;
    background: var(--card);
    box-shadow: 10px 12px 18px rgba(0,0,0,0.35);
    overflow: hidden;
    font-family: "Lato", sans-serif; color: var(--white);
  }
  .card--front { left: 92px; }
  .card--back { left: 634px; }

  .brand {
    position: absolute; top: 240px; left: 0; width: 100%;
    display: flex; flex-direction: column; align-items: center;
    color: var(--silver); font-weight: 700;
  }
  .brand__row { display: flex; align-items: center; gap: 14px; }
  .brand__dot { width: 22px; height: 22px; border-radius: 50%; background: var(--silver); }
  .brand__name { font-size: 56px; line-height: 64px; letter-spacing: 2px; text-transform: uppercase; }
  .brand__legal { margin-top: 6px; font-size: 17px; letter-spacing: 1px; }

  .icons {
    position: absolute; top: 460px; left: 0; width: 100%;
    display: flex; justify-content: center; gap: 10px;
  }
  .icons svg { width: 25px; height: 25px; }
  .rule { position: absolute; height: 2px; background: linear-gradient(90deg, transparent, var(--green) 20%, var(--green) 80%, transparent); }
  .rule--contact { top: 501px; left: 167px; width: 146px; }
  .contact {
    position: absolute; top: 520px; left: 0; width: 100%;
    text-align: center; font-size: 19px; line-height: 26.5px;
  }
  .address {
    position: absolute; top: 752px; left: 0; width: 100%;
    text-align: center; font-size: 19px; line-height: 27px;
  }
  .rule--left { top: 782px; left: 0; width: 118px; background: linear-gradient(90deg, transparent, var(--green) 40%); }
  .rule--right { top: 782px; right: 0; width: 118px; background: linear-gradient(90deg, var(--green) 60%, transparent); }

  .portrait {
    position: absolute; top: 0; left: 0; width: 100%; height: 640px;
    background: radial-gradient(ellipse 55% 60% at 50% 45%, #3a3430 0%, #24252c 55%, var(--card) 100%);
  }
  .brand--back { top: 646px; color: var(--green); }
  .brand--back .brand__name { font-size: 44px; line-height: 52px; }
  .brand--back .brand__dot { background: var(--green); width: 18px; height: 18px; }
  .person__name {
    position: absolute; top: 714px; left: 0; width: 100%; text-align: center;
    font-family: "Russo One", sans-serif; font-size: 35px; font-weight: 400; color: var(--grey); letter-spacing: 1px;
  }
  .person__title {
    position: absolute; top: 757px; left: 0; width: 100%; text-align: center;
    font-size: 23px; color: var(--white);
  }
  .rule--title { top: 798px; left: 196px; width: 88px; }
</style>
</head>
<body>
<div class="canvas">
  <section class="card card--front">
    <div class="brand">
      <div class="brand__row">
        <span class="brand__dot"></span>
        <span class="brand__name">Velmora</span>
      </div>
      <span class="brand__legal">Property Inspections, LLC</span>
    </div>
    <div class="icons">
      <svg viewBox="0 0 24 24" aria-label="Phone"><circle cx="12" cy="12" r="12" fill="var(--green)"/><path d="M8.5 6.5l2 2-1.2 1.5c.8 1.7 2 2.9 3.7 3.7l1.5-1.2 2 2-1.3 1.8c-3.8-.4-7.6-4.2-8-8z" fill="#fff"/></svg>
      <svg viewBox="0 0 24 24" aria-label="Email"><circle cx="12" cy="12" r="12" fill="var(--green)"/><rect x="6" y="8" width="12" height="8.5" rx="1" fill="#fff"/><path d="M6.5 8.5l5.5 4 5.5-4" stroke="var(--green)" stroke-width="1.2" fill="none"/></svg>
      <svg viewBox="0 0 24 24" aria-label="Website"><circle cx="12" cy="12" r="12" fill="var(--green)"/><g stroke="#fff" stroke-width="1.1" fill="none"><circle cx="12" cy="12" r="5.5"/><ellipse cx="12" cy="12" rx="2.4" ry="5.5"/><path d="M6.5 12h11M7.3 9.3h9.4M7.3 14.7h9.4"/></g></svg>
    </div>
    <div class="rule rule--contact"></div>
    <div class="contact">
      <p>480-555-0172</p>
      <p>glen@velmora-llc.example</p>
      <p>www.velmora-llc.example</p>
    </div>
    <div class="rule rule--left"></div>
    <div class="rule rule--right"></div>
    <div class="address">
      <p>48 Quarry Lane, Suite# B</p>
      <p>Tempe, AZ 85281</p>
    </div>
  </section>

  <section class="card card--back">
    <div class="portrait" role="img" aria-label="Portrait photo of the home inspector in a dark polo shirt"></div>
    <div class="brand brand--back">
      <div class="brand__row">
        <span class="brand__dot"></span>
        <span class="brand__name">Velmora</span>
      </div>
    </div>
    <h1 class="person__name">GLEN MIREWICK</h1>
    <p class="person__title">Home Inspector</p>
    <div class="rule rule--title"></div>
  </section>
</div>
</body>
</html>
```